Design a Dynamic and User-Friendly Website for kLobbyra: Revolutionize Visitor Management

Description of kLobbyra:

kLobbyra is an innovative online visitor management system designed to streamline the process of managing visitors in various organizational settings. Our system automates the check-in process, enhances security by keeping accurate visitor logs, and ensures compliance with local regulations through customizable features. With functionalities such as contactless sign-in, real-time notifications, visitor badge printing, and comprehensive reporting, kLobbyra provides a modern solution to traditional visitor management challenges.

Target Audience:

Our primary target audience includes businesses and institutions across Africa, starting with Nigeria. This includes corporate offices, educational institutions, healthcare facilities, and government buildings that are looking for efficient, secure, and scalable visitor management solutions. Our system is particularly tailored to meet the needs of facility managers, security personnel, and front desk staff who prioritize ease of use, data security, and operational efficiency. Additionally, kLobbyra aims to cater to IT managers looking for robust systems that can seamlessly integrate with existing organizational infrastructure.

Color Scheme:

While specific colors are not mandated, the chosen palette should convey trust and stability, growth and efficiency, and maintain a professional and clean appearance. The colors selected should harmonize to create a welcoming, secure, and efficient atmosphere.
Typography:

Use modern, sans-serif fonts for readability and a contemporary look. Primary text should be clear with high contrast against the background, and headings can be bold to create a hierarchical structure that is easy to navigate.
Imagery:

Photography: High-quality images that feature African professionals and contexts, illustrating diverse, professional scenarios relevant to our target industries (such as corporate offices, educational institutions, healthcare facilities). Photos should authentically represent the African demographic, showing interactions between people and technology, emphasizing the ease and security of the visitor management process.
Illustrations: Custom illustrations that should culturally resonate with African settings and characters, vividly depicting functionalities of kLobbyra such as scanning a QR code, receiving a visitor badge, or receiving alerts on a smartphone or desktop. These illustrations should adopt a style that complements the overall design aesthetic of the site.
Layout and Design Elements:

A clean, minimalistic layout that focuses on usability with easy navigation paths for all user types.
Use cards or tiles for different sections such as features, testimonials, or case studies, which can help organize information cleanly and attractively.
Consider interactive elements like hover effects, animated transitions for loading elements, and subtle animations in illustrations to make the user experience dynamic and engaging.
Overall Theme:

The theme should be professional and welcoming, reflecting a high-tech solution that is approachable for users with varying levels of tech expertise. The design should instill confidence in the security and efficiency of the system, while also being culturally appropriate and user-friendly to encourage interaction and exploration of the site’s content.
This style and theme guide emphasizes flexibility in color usage while maintaining clear directives on the emotional and functional responses the design should invoke, ensuring it aligns with the values and needs of kLobbyra's target audience.

What websites can designers draw inspiration from?
List websites you like and describe what you like about them.

https://tallodesk.com/en-usremove
same industry so you can see their approaches to marketing to similar customers - granted their target is not specific to african market Very clean design and straight to the point. Their feature set is closest to our feature set.
http://www.gatrumo.comremove
clean design and straight to the point
http://vennatrak.comremove

Home Page
-------------------
Main Goal: Encourage visitors to start their 15-day free trial, effectively converting them into leads or potential customers.

Content Layout:
Hero Section: Engaging hero image or video that shows the kLobbyra system in action, with clear, prominent call-to-action (CTA) buttons for "Start your 15 day free trial" and secondary CTA for "Buy now"

Product Overview: Quick introduction to what kLobbyra is and its key benefits, such as enhanced security, easy integration, and improved operational efficiency.

Features Highlight: Brief visuals or icons depicting major features like contactless sign-in, real-time alerts, and comprehensive reporting.

How It Works: A concise step-by-step guide or graphic explaining how to get started with kLobbyra.

CTA Section: A more detailed call to action for starting the free trial,
if they want a more hands on guide allow them to schedule a demo and if they are ready click purchase to buy now.
Footer: Navigation links to other site sections, social media links, and legal information.

-------------------
Pricing Page
-------------------
Main Goal: Clearly convey the pricing structure in a way that users can easily understand and compare options based on their location and specific needs.

Content Layout:

Pricing Introduction: Explain the subscription model, highlighting the flexibility and scalability of the service (i.e., per location and additional tablets).

Country-Specific Pricing Tabs: Tabs or a dropdown menu allowing users to choose their country (Nigeria, Ghana, South Africa, Kenya) to view localized pricing in the respective currencies (NGN, GHS, ZAR, KES).
Subscription Per Location: Detailed pricing for managing a single location, with benefits listed beside the price

Tablets and Data Plans: A clear breakdown of the cost per tablet and the associated wireless data plans, including bulk discount options if applicable.
Interactive Pricing Calculator: A tool that allows users to calculate their monthly cost based on the number of locations and tablets they plan to use.

Add ons - for hardware, etc

FAQs: A section dedicated to frequently asked questions specifically about pricing, billing cycles, and cancellation policies.

CTA: Strong call to action for starting a free trial, with an emphasis on the ease of signing up and the no-commitment nature of the trial.

Footer: Standard navigational links, contact information, and social media buttons.

-------------------
Feature Page Template
-------------------
Main Goal: To detail individual features of kLobbyra, demonstrating the functionality and benefits to help prospective clients understand the value provided.

Content Layout:
Feature Introduction: Large title with a succinct description of the feature.

In-depth Details: Bullet points or short paragraphs explaining the feature, supported by relevant images or icons.

Use Case Scenario: Real-world application or a mini-case study showing the feature in action.

Benefit Summary: A list or graphic illustrating the benefits of the feature.

CTA: Prompt to try this feature via signup or schedule a demo speak with a sales representative.

Footer: Standard links and social media connections.

-------------------
Blog Page
-------------------
Main Goal: To engage current and prospective clients with useful content, position kLobbyra as a thought leader in the visitor management space, and improve SEO rankings.

Content Layout:
Featured Article: Highlight a recent or popular post prominently at the top.

Article List: Thumbnails and summaries of additional articles with clear categorization (e.g., Tips, Case Studies, Industry News).

Search and Filter Tools: Allow users to filter blog posts by topic, date, etc.

Newsletter Signup: Encourage visitors to subscribe to updates.
Social Share Buttons: Enable easy sharing of articles.
Footer: Include a comprehensive footer with navigational links and contact info.

Generic Content Page (e.g., Contact Us, About Us)
------------------------------
Main Goal: To provide essential information about the kLobbyra company or to facilitate contact with the company.

Content Layout:
Page Title and Introduction: Clear heading with a brief paragraph summarizing the page’s purpose.

Main Content Area: Detailed content appropriate to the page (e.g., company history, team bios for About Us; contact form, map, and helpline numbers for Contact Us).

Sidebar/Additional Elements: For Contact Us, include operational hours or a quick FAQ. For About Us, list awards or recognitions.

CTA: Depending on the page, direct users to other parts of the site (e.g., careers page link on About Us, newsletter sign-up on Contact Us).
Footer: Standard footer with expanded company details if on the Contact Us page.

Coding

```html
<!DOCTYPE html>
<html lang="en">
<head>
<meta charset="utf-8">
<title>kLobbyra — Visitor Management</title>
<link href="https://fonts.googleapis.com/css2?family=Outfit:wght@600;700;800&family=Poppins:wght@300;400;500;600&display=swap" rel="stylesheet">
<style>
:root{
  --ink:#0d0d12;
  --night:#07060d;
  --blue:#2f5bff;
  --violet:#7b2ff7;
  --purple:#a34bf0;
  --lav:#efe8fb;
  --grey:#55555f;
  --muted:#8a8a96;
  --line:#d9d9e0;
  --white:#ffffff;
  --head:"Outfit",sans-serif;
  --body:"Poppins",sans-serif;
}
*{margin:0;padding:0;box-sizing:border-box}
html,body{width:1200px;height:3906px;overflow:hidden}
body{position:relative;background:var(--white);font-family:var(--body);color:var(--ink)}
.abs{position:absolute}
.grad-text{background:linear-gradient(90deg,var(--blue),var(--violet));-webkit-background-clip:text;background-clip:text;color:transparent}

/* hero */
.hero{left:0;top:0;width:1200px;height:600px;background:
  radial-gradient(ellipse 420px 360px at 120px 330px,rgba(90,40,210,.55),transparent 70%),
  radial-gradient(ellipse 500px 300px at 380px 120px,rgba(40,40,150,.45),transparent 70%),
  radial-gradient(ellipse 320px 260px at 1150px 380px,rgba(120,40,200,.35),transparent 70%),
  var(--night);color:var(--white)}
.brand{font-family:var(--body);font-weight:400;font-size:22px;display:flex;align-items:center;gap:6px}
.brand i{width:18px;height:18px;border:2px solid currentColor;border-radius:50%;display:inline-block}
.nav a{position:absolute;top:23px;font-size:11px;color:var(--white);text-decoration:none}
.nav .sep{position:absolute;top:24px;width:1px;height:12px;background:rgba(255,255,255,.35)}
.btn-login{left:916px;top:15px;width:80px;height:31px;border-radius:16px;background:var(--white);color:var(--ink);font-size:11px;font-weight:600;display:flex;align-items:center;justify-content:center}
.eyebrow{font-size:9px;letter-spacing:5px;text-transform:uppercase;display:flex;align-items:center;gap:8px}
.eyebrow .rule{width:50px;height:1px;background:currentColor;opacity:.6}
.hero h1{left:155px;top:192px;font-family:var(--head);font-weight:700;font-size:45px;line-height:48px;letter-spacing:-1px}
.hero p{left:156px;top:300px;width:420px;font-size:11.5px;line-height:16px;color:#e6e4f0}
.btn{display:flex;align-items:center;justify-content:center;border-radius:20px;font-size:11px;font-weight:600}
.btn-trial{left:158px;top:393px;width:205px;height:37px;background:var(--white);color:var(--ink)}
.btn-buy{left:375px;top:393px;width:106px;height:37px;border:1.5px solid var(--violet);color:var(--white);background:rgba(0,0,0,.4)}
.dot{border:3px solid var(--white);border-radius:50%;width:12px;height:12px}
.dot.s{width:4px;height:4px;border:0;background:var(--white)}
.social-v{width:24px;height:24px;border:1px solid rgba(255,255,255,.7);border-radius:50%}
.device{left:663px;top:79px;width:384px;height:421px;border-radius:14px;background:linear-gradient(160deg,#f4f4f6 0%,#d8d8de 55%,#2c2c33 100%);transform:perspective(900px) rotateY(-14deg)}
.vtext{font-size:10px;transform:rotate(90deg);transform-origin:left top;white-space:nowrap}

/* band */
.band{left:0;top:600px;width:1200px;height:43px;background:linear-gradient(90deg,#5f6cf5,#8b5cf6 50%,#c34ff0);color:var(--white);font-family:var(--head);font-weight:700;font-size:17px;letter-spacing:-.3px}
.band span{position:absolute;top:11px}

/* trusted */
.trusted{left:0;top:698px;width:1200px;text-align:center;font-size:10px}
.partner{top:744px;height:44px;display:flex;align-items:center;justify-content:center;gap:8px;color:#6a6a74;font-family:var(--body);font-weight:500;font-size:12px;line-height:15px;text-align:left}
.partner .mark{width:10px;height:10px;border-radius:50%;background:#c9c9d0;flex:none}
.partner-sep{top:750px;width:1px;height:34px;background:#ddd}

/* section titles */
.label{font-size:9px;letter-spacing:5px;color:var(--grey);text-transform:uppercase;display:flex;align-items:center;gap:10px}
.label .rule{width:60px;height:1px;background:var(--grey)}
.h2{font-family:var(--head);font-weight:700;font-size:44px;letter-spacing:-1.2px;line-height:54px}

.tablet{left:146px;top:991px;width:423px;height:314px;border-radius:14px;background:linear-gradient(150deg,#f7f3fd,#e9e1f7 60%,#d7d2e0);box-shadow:0 16px 30px rgba(0,0,0,.18)}
.about-text{left:614px;width:420px;font-size:11.5px;line-height:16.5px;color:#333}
.quote{top:1024px;border-left:2px solid var(--violet);padding-left:8px;color:var(--ink)}
.btn-read{left:610px;top:1235px;width:117px;height:36px;background:linear-gradient(90deg,var(--blue),var(--violet));color:var(--white)}

/* features */
.features{left:0;top:1438px;width:1200px;height:751px;background:
  radial-gradient(ellipse 380px 300px at 60px 40px,rgba(160,140,240,.45),transparent 70%),
  radial-gradient(ellipse 360px 340px at 1180px 620px,rgba(220,160,240,.55),transparent 70%),
  #f3f2f6}
.feat{width:200px}
.feat svg{position:absolute;left:-39px;top:0}
.feat h4{font-size:13px;font-weight:500;margin-bottom:8px}
.feat p{font-size:12px;line-height:18px;color:#555}
.feat-card{left:622px;top:1685px;width:220px;height:114px;background:var(--white);border-radius:8px;border:1.5px solid #d7c4f5;box-shadow:0 8px 20px rgba(120,80,200,.15)}

/* how */
.photo{left:0;top:2420px;width:546px;height:390px;background:linear-gradient(160deg,#d6d6da,#8d8a8f 55%,#2b2729)}
.step{background:var(--white);border-radius:18px;box-shadow:0 10px 30px rgba(0,0,0,.06)}
.step.outline{border:1.5px solid #e2e2ea;box-shadow:none}
.step .num{position:absolute;font-family:var(--head);font-weight:800;font-size:92px;line-height:1;letter-spacing:-3px}
.step h5{position:absolute;font-size:15px;font-weight:600}
.step p{position:absolute;font-size:9.5px;line-height:17px;color:#444;width:250px}

/* contact */
.form-card{left:196px;top:3030px;width:811px;height:427px;border-radius:26px;background:
  radial-gradient(ellipse 160px 140px at 40px 20px,rgba(150,110,240,.6),transparent 70%),
  radial-gradient(ellipse 170px 150px at 790px 410px,rgba(150,110,240,.6),transparent 70%),
  #f2f2f4}
.field{font-size:10px;color:var(--muted);border-bottom:1px solid #cfcfd5;padding-bottom:10px}
.btn-submit{left:275px;top:3365px;width:116px;height:35px;background:linear-gradient(90deg,var(--blue),var(--violet));color:var(--white)}

/* footer */
.footer{left:0;top:3574px;width:1200px;height:332px;background:
  radial-gradient(ellipse 500px 260px at 1150px 40px,rgba(110,40,190,.45),transparent 70%),
  radial-gradient(ellipse 400px 220px at 380px 0,rgba(40,40,130,.4),transparent 70%),
  var(--night);color:var(--white)}
.fhead{font-size:13px;font-weight:600}
.flinks{list-style:none;font-size:10.5px;line-height:18.5px}
.flinks li::before{content:"» ";color:#aaa}
.fcontact{font-size:11px;font-weight:600}
.fcontact small{display:block;font-weight:400;font-size:10px;color:#ddd}
.fsoc{width:24px;height:24px;border:1px solid rgba(255,255,255,.6);border-radius:50%}
.nl-input{left:850px;top:3718px;width:166px;height:28px;border-radius:14px;background:var(--white);color:#999;font-size:8px;padding:9px 18px}
.nl-btn{left:850px;top:3753px;width:106px;height:29px;background:var(--white);color:var(--ink)}
.bottom{left:0;top:3880px;width:1200px;height:26px;background:#1a1a1f;color:#ddd;font-size:10px}
</style>
</head>
<body>

<!-- HERO -->
<section class="abs hero">
  <div class="abs brand" style="left:152px;top:18px"><i></i>kLobbyra</div>
  <nav class="nav">
    <a style="left:610px">Home</a><span class="sep" style="left:660px"></span>
    <a style="left:684px">Pricing</a><span class="sep" style="left:737px"></span>
    <a style="left:763px">Our Feature</a><span class="sep" style="left:840px"></span>
    <a style="left:863px">Blog</a>
  </nav>
  <div class="abs btn btn-login">Log In</div>

  <div class="abs dot" style="left:172px;top:105px"></div>
  <div class="abs dot" style="left:588px;top:137px"></div>
  <div class="abs dot" style="left:23px;top:496px"></div>
  <div class="abs dot" style="left:428px;top:509px"></div>
  <div class="abs dot s" style="left:284px;top:80px;opacity:.6"></div>
  <div class="abs dot s" style="left:299px;top:558px"></div>
  <div class="abs dot s" style="left:1118px;top:533px"></div>

  <div class="abs vtext" style="left:66px;top:172px">Follow Us</div>
  <div class="abs" style="left:60px;top:232px;width:1px;height:50px;background:rgba(255,255,255,.5)"></div>
  <div class="abs social-v" style="left:48px;top:300px" aria-label="Social link"></div>
  <div class="abs social-v" style="left:48px;top:335px" aria-label="Social link"></div>
  <div class="abs social-v" style="left:48px;top:370px" aria-label="Social link"></div>

  <div class="abs eyebrow" style="left:156px;top:165px">Welcome to kLobbyra <span class="rule"></span></div>
  <h1 class="abs">Managing Visitors<br>In Various <span class="grad-text">Health Apps</span></h1>
  <p class="abs">Effectively managing visitors in organizational settings involves implementing secure check-in procedures and providing clear guidance to ensure a seamless and welcoming experience while maintaining security protocols.</p>
  <div class="abs btn btn-trial">Start your 15 day free trial</div>
  <div class="abs btn btn-buy">Buy now</div>

  <div class="abs device" role="img" aria-label="Curved monitor showing the kLobbyra settings dashboard"></div>

  <div class="abs vtext" style="left:1160px;top:172px">info@mailora.com</div>
  <div class="abs" style="left:1149px;top:305px;width:10px;height:1px;background:rgba(255,255,255,.5)"></div>
  <div class="abs vtext" style="left:1160px;top:358px">615.000.0142</div>
  <svg class="abs" style="left:1148px;top:422px" width="12" height="12" viewBox="0 0 24 24"><path d="M6 3l4 4-2 3a12 12 0 0 0 6 6l3-2 4 4-3 3C10 21 3 14 3 6z" fill="#b05cf2"/></svg>
</section>

<!-- BAND -->
<div class="abs band">
  <span style="left:24px">DEVELOPERS</span>
  <span style="left:179px">EASY INTEGRATION</span>
  <span style="left:392px">BEST RESEARCHERS</span>
  <span style="left:614px">IMPROVED OPERATIONAL</span>
  <span style="left:868px">FASTER WAY</span>
  <span style="left:1027px">EASY INTEGRATION</span>
</div>

<!-- TRUSTED -->
<div class="abs trusted">Trusted by the Best researcher and pofessionals</div>
<div class="abs partner" style="left:225px;width:180px"><span class="mark"></span>Halvern<br>Medical School</div>
<div class="abs partner-sep" style="left:405px"></div>
<div class="abs partner" style="left:418px;width:130px"><span class="mark"></span>Ucora<br>Health</div>
<div class="abs partner-sep" style="left:556px"></div>
<div class="abs partner" style="left:590px;width:140px"><span class="mark"></span>Northfield<br>University</div>
<div class="abs partner-sep" style="left:744px"></div>
<div class="abs partner" style="left:755px;width:120px"><span class="mark"></span>Westbrook<br>University</div>
<div class="abs partner-sep" style="left:880px"></div>
<div class="abs partner" style="left:890px;width:110px"><span class="mark"></span>Stanwell<br>University</div>

<!-- ABOUT -->
<div class="abs label" style="left:490px;top:863px"><span class="rule"></span>About us<span class="rule"></span></div>
<h2 class="abs h2" style="left:0;top:885px;width:1200px;text-align:center">Learn More About Us and <span class="grad-text">Our Mission</span></h2>
<div class="abs tablet" role="img" aria-label="Tablet showing the kLobbyra account login screen"></div>
<p class="abs about-text quote">It is a long established fact that a reader will be distracted by the read able content of a page when looking at its layout.</p>
<p class="abs about-text" style="top:1078px">Lorem Ipsum is simply dummy text of the printing and typesetting indu stry. Lorem Ipsum has been the industry's standard dummy text ever since the 1500s, when an unknown printer took a galley of type and scrambled it to make a type specimen book.</p>
<p class="abs about-text" style="top:1162px">It is a long established fact that a reader will be distracted by the read able content of a page when looking at its layout. The point of using Lorem Ipsum is that it has a more-or-less normal distribution of letters.</p>
<div class="abs btn btn-read">Read More</div>

<!-- FEATURES -->
<section class="abs features"></section>
<div class="abs label" style="left:133px;top:1528px">Features<span class="rule"></span></div>
<h2 class="abs h2" style="left:131px;top:1550px">Unveiling Key Features of<br><span class="grad-text">Our Offering</span><span style="color:var(--violet)">!</span></h2>
<p class="abs" style="left:754px;top:1573px;width:300px;font-size:11.5px;line-height:16.5px;color:#444">It is a long established fact that a reader will be distracted by the readable content of a page when looking at its layout.</p>
<div class="abs feat-card"></div>

<svg width="0" height="0" style="position:absolute">
  <defs>
    <symbol id="ico" viewBox="0 0 28 28"><rect x="4" y="6" width="20" height="16" rx="3" fill="none" stroke="#6b6b78" stroke-width="1.6"/><circle cx="14" cy="13" r="3" fill="none" stroke="#6b6b78" stroke-width="1.6"/><path d="M9 22c1-3 3-4 5-4s4 1 5 4" fill="none" stroke="#6b6b78" stroke-width="1.6"/></symbol>
  </defs>
</svg>

<div class="abs feat" style="left:180px;top:1705px"><svg width="28" height="28"><use href="#ico"/></svg><h4>Lorem Ipsum</h4><p>It is a long established fact that a reader will be distracted.</p></div>
<div class="abs feat" style="left:429px;top:1705px"><svg width="28" height="28"><use href="#ico"/></svg><h4>Lorem Ipsum</h4><p>It is a long established fact that a reader will be distracted.</p></div>
<div class="abs feat" style="left:672px;top:1705px"><svg width="28" height="28"><use href="#ico"/></svg><h4>Lorem Ipsum</h4><p>It is a long established fact that a reader will be distracted.</p></div>
<div class="abs feat" style="left:916px;top:1705px"><svg width="28" height="28"><use href="#ico"/></svg><h4>Lorem Ipsum</h4><p>It is a long established fact that a reader will be distracted.</p></div>

<div class="abs feat" style="left:180px;top:1843px"><svg width="28" height="28"><use href="#ico"/></svg><h4>Lorem Ipsum</h4><p>It is a long established fact that a reader will be distracted.</p></div>
<div class="abs feat" style="left:429px;top:1843px"><svg width="28" height="28"><use href="#ico"/></svg><h4>Lorem Ipsum</h4><p>It is a long established fact that a reader will be distracted.</p></div>
<div class="abs feat" style="left:672px;top:1843px"><svg width="28" height="28"><use href="#ico"/></svg><h4>Lorem Ipsum</h4><p>It is a long established fact that a reader will be distracted.</p></div>
<div class="abs feat" style="left:916px;top:1843px"><svg width="28" height="28"><use href="#ico"/></svg><h4>Lorem Ipsum</h4><p>It is a long established fact that a reader will be distracted.</p></div>

<div class="abs feat" style="left:180px;top:1978px"><svg width="28" height="28"><use href="#ico"/></svg><h4>Lorem Ipsum</h4><p>It is a long established fact that a reader will be distracted.</p></div>
<div class="abs feat" style="left:429px;top:1978px"><svg width="28" height="28"><use href="#ico"/></svg><h4>Lorem Ipsum</h4><p>It is a long established fact that a reader will be distracted.</p></div>
<div class="abs feat" style="left:672px;top:1978px"><svg width="28" height="28"><use href="#ico"/></svg><h4>Lorem Ipsum</h4><p>It is a long established fact that a reader will be distracted.</p></div>
<div class="abs feat" style="left:916px;top:1978px"><svg width="28" height="28"><use href="#ico"/></svg><h4>Lorem Ipsum</h4><p>It is a long established fact that a reader will be distracted.</p></div>

<!-- HOW IT WORKS -->
<div class="abs label" style="left:133px;top:2283px">How it work<span class="rule"></span></div>
<h2 class="abs h2" style="left:131px;top:2307px;line-height:48px">Unraveling<br>How It <span class="grad-text">Work</span><span style="color:var(--violet)">!</span></h2>
<div class="abs photo" role="img" aria-label="Photo of two African professionals checking in at a front desk with a laptop"></div>

<svg class="abs" style="left:550px;top:2300px" width="600" height="500" viewBox="0 0 600 500" fill="none">
  <path d="M80 60C20 120 20 230 90 300" stroke="#e2e2ea" stroke-width="1.2"/>
  <path d="M520 200c60 40 70 160 10 210" stroke="#e2e2ea" stroke-width="1.2"/>
  <path d="M80 250l34 8-20 12z" fill="#7ea0ff"/>
  <path d="M470 410l34-6-14 20z" fill="#7ea0ff"/>
</svg>

<div class="abs step" style="left:634px;top:2300px;width:395px;height:149px">
  <span class="num grad-text" style="left:18px;top:30px">01</span>
  <h5 style="left:123px;top:28px">Concept Note</h5>
  <p style="left:123px;top:54px">Lorem Ipsum is simply dummy text of the printing and typesetting industry. Lorem Ipsum has been the industry's standard dummy text ever since the 1500s, when an unknown.</p>
</div>
<div class="abs step outline" style="left:672px;top:2464px;width:398px;height:151px">
  <span class="num" style="left:14px;top:30px;color:#dcdce0">02</span>
  <h5 style="left:135px;top:24px">Accompagnement</h5>
  <p style="left:135px;top:52px">Lorem Ipsum is simply dummy text of the printing and typesetting industry. Lorem Ipsum has been the industry's standard dummy text ever since the 1500s, when an unknown.</p>
</div>
<div class="abs step outline" style="left:634px;top:2632px;width:398px;height:150px">
  <span class="num" style="left:14px;top:30px;color:#dcdce0">03</span>
  <h5 style="left:138px;top:24px">Production &amp; Deployment</h5>
  <p style="left:138px;top:52px">Lorem Ipsum is simply dummy text of the pri nting and typesetting industry. Lorem Ipsum has been the industry's standard dummy text ever since the 1500s, when an unknown.</p>
</div>

<!-- CONTACT -->
<div class="abs label" style="left:0;top:2917px;width:1200px;justify-content:center"><span class="rule"></span>Conatact us<span class="rule"></span></div>
<h2 class="abs h2" style="left:0;top:2939px;width:1200px;text-align:center">Get Started <span class="grad-text">Now</span></h2>
<div class="abs form-card"></div>
<div class="abs" style="left:273px;top:3097px;font-size:26px;font-weight:400">Fil Out the Form Below</div>
<div class="abs" style="left:273px;top:3139px;font-size:11.5px;color:#444">Switching to fresh accountancy couldn't be easier, we do it all for you..</div>
<div class="abs field" style="left:285px;top:3197px;width:292px">First Name*</div>
<div class="abs field" style="left:645px;top:3197px;width:291px">First Name*</div>
<div class="abs field" style="left:285px;top:3251px;width:292px">Email Address*</div>
<div class="abs field" style="left:645px;top:3251px;width:291px">Phone Number*</div>
<div class="abs field" style="left:285px;top:3307px;width:651px">Message*</div>
<div class="abs btn btn-submit">Submit Now</div>

<!-- FOOTER -->
<footer class="abs footer"></footer>
<div class="abs brand" style="left:174px;top:3690px;color:#fff"><i></i>kLobbyra</div>
<p class="abs" style="left:174px;top:3733px;width:240px;font-size:11px;line-height:16px;color:#eee">It is a long established fact that a reader will be distracted by the readable content of a page when.</p>
<div class="abs fsoc" style="left:174px;top:3806px" aria-label="Social link"></div>
<div class="abs fsoc" style="left:206px;top:3806px" aria-label="Social link"></div>
<div class="abs fsoc" style="left:238px;top:3806px" aria-label="Social link"></div>
<div class="abs fsoc" style="left:270px;top:3806px" aria-label="Social link"></div>

<div class="abs fhead" style="left:481px;top:3677px;color:#fff">Home</div>
<ul class="abs flinks" style="left:481px;top:3703px;color:#fff">
  <li>About</li><li>Features</li><li>Voice</li><li>Price</li><li>Access</li><li>FAQ</li>
</ul>

<div class="abs fhead" style="left:627px;top:3677px;color:#fff">Contact Us</div>
<svg class="abs" style="left:627px;top:3712px" width="12" height="12" viewBox="0 0 24 24"><path d="M6 3l4 4-2 3a12 12 0 0 0 6 6l3-2 4 4-3 3C10 21 3 14 3 6z" fill="#fff"/></svg>
<div class="abs fcontact" style="left:650px;top:3708px;color:#fff">Call Us :<small>+81-80-0000-0142</small></div>
<svg class="abs" style="left:627px;top:3756px" width="12" height="10" viewBox="0 0 24 18"><rect x="1" y="1" width="22" height="16" rx="2" fill="#fff"/><path d="M2 2l10 8 10-8" stroke="#07060d" stroke-width="2" fill="none"/></svg>
<div class="abs fcontact" style="left:650px;top:3750px;color:#fff">Email Us :<small>hello@klobbyra.io</small></div>
<svg class="abs" style="left:628px;top:3796px" width="11" height="14" viewBox="0 0 20 26"><path d="M10 0a9 9 0 0 0-9 9c0 7 9 17 9 17s9-10 9-17a9 9 0 0 0-9-9z" fill="#fff"/><circle cx="10" cy="9" r="3" fill="#07060d"/></svg>
<div class="abs fcontact" style="left:650px;top:3790px;color:#fff">Location :<small>Lindqvist Vej 48, 2750<br>Nordby</small></div>

<div class="abs fhead" style="left:850px;top:3677px;color:#fff">Newsletter</div>
<div class="abs nl-input">Enter Your Email</div>
<div class="abs btn nl-btn">Subscribe</div>

<div class="abs bottom">
  <span class="abs" style="left:170px;top:7px">Copyright(C) kLobbyra. All Rights Reserved.</span>
  <span class="abs" style="left:857px;top:7px">License And Subscription Terms</span>
</div>

</body>
</html>
```